Business Card Design

I need a business card for my Heating / Cooling Business. I've been in the business for 28 years. The name of the company is "Tom's Heating and Cooling".
Designers, I've attached an old business card we've used to copy the information.
Take off 15 years of experience
Industry/Entity Type
Business
Contact Information for Business Card
Gene Waltham and Lorna Waltham(740)-795-4758

```html
<!DOCTYPE html>
<html lang="en">
<head>
<meta charset="utf-8">
<title>Tom's Heating and Cooling – Business Card</title>
<link rel="stylesheet" href="https://fonts.googleapis.com/css2?family=Open+Sans:wght@400;600;700&display=swap">
<style>
  :root {
    --hot-red: #e8212b;
    --cool-blue: #0a7fc6;
    --ink: #3b3b3b;
    --muted: #555555;
    --paper: #ffffff;
    --backdrop: #ffffff;
  }
  * { margin: 0; padding: 0; box-sizing: border-box; }
  html, body {
    width: 1200px; height: 790px; overflow: hidden;
    background: var(--backdrop);
    font-family: "Open Sans", Arial, sans-serif;
  }
  .canvas { position: relative; width: 1200px; height: 790px; }
  .card {
    position: absolute; left: 199px; top: 190px;
    width: 805px; height: 408px;
    background: var(--paper);
    box-shadow: 2px 3px 5px rgba(0,0,0,0.45);
    overflow: hidden;
  }
  .card-art { position: absolute; inset: 0; }
  .tagline {
    position: absolute; left: 351px; top: 13px;
    color: var(--paper); font-weight: 700; font-size: 15px;
  }
  .services {
    position: absolute; left: 9px; top: 95px;
    list-style: none; color: var(--paper); font-size: 13.6px; line-height: 19px;
    white-space: nowrap;
  }
  .services .service-lead { font-size: 15px; }
  .company-name {
    position: absolute; left: 348px; top: 144px;
    font-size: 31px; font-weight: 700; color: var(--ink);
    letter-spacing: -0.3px;
    text-shadow: 2px 3px 4px rgba(0,0,0,0.45);
  }
  .contact { position: absolute; font-size: 12px; color: var(--muted); white-space: nowrap; }
  .contact-icon { position: absolute; fill: var(--muted); }
</style>
</head>
<body>
<div class="canvas">
  <div class="card">
    <svg class="card-art" width="805" height="408" viewBox="0 0 805 408" aria-hidden="true">
      <defs>
        <linearGradient id="sweep-main" x1="0" y1="0" x2="0" y2="1">
          <stop offset="0" stop-color="var(--hot-red)"/>
          <stop offset="0.45" stop-color="#8e5a78"/>
          <stop offset="1" stop-color="var(--cool-blue)"/>
        </linearGradient>
        <linearGradient id="sweep-corner" x1="1" y1="0" x2="0.6" y2="1">
          <stop offset="0" stop-color="var(--cool-blue)"/>
          <stop offset="0.55" stop-color="#8e5a78"/>
          <stop offset="1" stop-color="var(--hot-red)"/>
        </linearGradient>
      </defs>
      <path class="sweep-main" d="M0,0 H805 C520,30 180,200 0,408 Z" fill="url(#sweep-main)"/>
      <path class="sweep-corner" d="M505,408 C650,385 770,320 805,258 V408 Z" fill="url(#sweep-corner)"/>
      <circle class="corner-dot" cx="10" cy="10" r="10" fill="var(--paper)"/>
      <circle class="corner-dot" cx="797" cy="400" r="5" fill="var(--paper)"/>
    </svg>

    <div class="tagline">Certified Repairman</div>
    <ul class="services">
      <li>Professional mobile home installation</li>
      <li class="service-lead">Small appliance repair</li>
      <li>Installation &amp; Service</li>
      <li>Car air conditioning</li>
      <li class="service-lead">Refrigeration</li>
      <li>Plumbing</li>
    </ul>

    <div class="company-name">Tom's Heating and Cooling</div>

    <svg class="contact-icon" style="left:205px;top:216px" width="30" height="28" viewBox="0 0 30 28" aria-hidden="true">
      <path d="M15,1 L29,14 L26,14 L26,27 L18,27 L18,18 L12,18 L12,27 L4,27 L4,14 L1,14 Z M7,15 V24 H9 V15 H21 V24 H23 V15 L15,7 Z"/>
    </svg>
    <div class="contact" style="left:244px;top:231px">48210 Maple Ridge Road, Cedar Hollow, Ohio 43017</div>

    <svg class="contact-icon" style="left:163px;top:250px" width="30" height="30" viewBox="0 0 30 30" aria-hidden="true">
      <g fill="none" stroke="var(--muted)" stroke-width="2.4">
        <circle cx="13" cy="13" r="11"/>
        <ellipse cx="13" cy="13" rx="5" ry="11"/>
        <path d="M2,13 H24 M4,7 H22 M4,19 H18"/>
      </g>
      <path d="M16,15 L28,21 L23,22 L26,28 L24,29 L21,23 L17,26 Z"/>
    </svg>
    <div class="contact" style="left:206px;top:265px">www.tomsheatcool.com</div>

    <svg class="contact-icon" style="left:122px;top:290px" width="30" height="22" viewBox="0 0 30 22" aria-hidden="true">
      <rect x="1.2" y="1.2" width="27.6" height="19.6" fill="none" stroke="var(--muted)" stroke-width="2.4"/>
      <path d="M2,2 L15,13 L28,2 M2,20 L11,11 M28,20 L19,11" fill="none" stroke="var(--muted)" stroke-width="2"/>
    </svg>
    <div class="contact" style="left:162px;top:299px">service@tomsheatcool.com</div>

    <svg class="contact-icon" style="left:86px;top:327px" width="18" height="30" viewBox="0 0 18 30" aria-hidden="true">
      <rect x="5" y="0" width="3" height="5"/>
      <rect x="1" y="4" width="16" height="25" rx="3"/>
      <rect x="4" y="7" width="10" height="9" fill="var(--paper)"/>
      <circle cx="9" cy="23" r="2" fill="var(--paper)"/>
    </svg>
    <div class="contact" style="left:114px;top:340px">Gene Waltham and Lorna Waltham(612)-438-2091</div>
  </div>
</div>
</body>
</html>
```